TULVO -Box for Tisanes( Tea made from Herbs & fruits)

We would like to start a new brand called " Tulvo" which will have 7 variants of tisanes ( basically teas made from plant parts) . These are all colorful boxes and you could use the ingredient photos and put on the box. Each box will have 20 pyramid  tea bags
I have attached the
1) actual pic of the loose tea ( total 5 types)
2) We will pack this in Pyramid Bags. I have attached picture of the Pyramid bag packaging
3) Some ideas about how the box should look like ( from other brands)
4) there is also a key line to follow for the sizing
5) leave space for Nutritional information , ingredients etc

Online b2c

```html
<!DOCTYPE html>
<html lang="en">
<head>
<meta charset="utf-8">
<title>Tulvo Chocolate Truffle – Box Panels</title>
<link rel="stylesheet" href="https://fonts.googleapis.com/css2?family=Baloo+2:wght@700;800&family=Fira+Sans+Condensed:ital,wght@0,400;0,600;1,400;1,600&family=Caveat:wght@700&display=swap">
<style>
  :root {
    --bg: #f4f3ef;
    --peach-light: #f8dcc6;
    --peach: #f2c7a8;
    --green-dark: #2f5a1c;
    --green-text: #4a7432;
    --ink: #4b4036;
    --rule: #8b7c6e;
    --yellow: #f1b823;
    --art-top: #d9b49a;
    --art-mid: #e3bfa4;
    --art-bottom: #efd0b8;
  }
  * { box-sizing: border-box; margin: 0; padding: 0; }
  html, body { width: 1200px; height: 800px; overflow: hidden; background: var(--bg); }
  body { position: relative; font-family: "Fira Sans Condensed", sans-serif; color: var(--ink); }

  .box-net { position: absolute; left: 190px; top: 110px; display: flex; height: 580px; }

  /* ---------- side panel ---------- */
  .side-panel {
    width: 320px; height: 100%;
    background: linear-gradient(180deg, var(--peach-light), var(--peach));
    border-top: 3px solid #d8382f;
    display: flex; gap: 10px; padding: 16px 10px 14px 12px;
    font-size: 7.6px; line-height: 1.3;
  }
  .info-column { flex: 1.1; }
  .legal-column { flex: 1; padding-top: 26px; }
  .category { color: var(--green-text); font-weight: 600; font-size: 9px; }
  .variant-name { color: var(--green-text); font-weight: 600; font-size: 10.5px; margin-bottom: 6px; }
  .label { font-weight: 600; }
  .ingredients { margin-bottom: 8px; }

  .nutrition { width: 100%; border-collapse: collapse; font-size: 7px; }
  .nutrition th, .nutrition td { border: 0.6px solid var(--rule); padding: 1.5px 3px; text-align: left; font-weight: 400; }
  .nutrition .table-title { text-align: center; font-weight: 600; font-size: 8px; }
  .nutrition td.num { text-align: right; }
  .nutrition .indent { padding-left: 9px; }
  .nutrition .foot { font-size: 6.6px; border: none; padding-top: 3px; }

  .legal-block { margin-bottom: 8px; }
  .cert-mark { display: block; width: 22px; height: 13px; border: 1px solid #b8a090; border-radius: 2px; margin: 6px auto 3px; }
  .lic { text-align: center; margin-bottom: 10px; }
  .consumer-care { border: 0.6px solid var(--rule); padding: 4px 5px; margin-top: 8px; }
  .consumer-care h4 { text-align: center; font-size: 7.8px; font-weight: 600; margin-bottom: 4px; }
  .care-row { display: flex; align-items: center; gap: 4px; margin: 3px 0; }
  .care-row svg { width: 8px; height: 8px; flex: none; }

  /* ---------- front panel ---------- */
  .front-panel {
    position: relative; width: 500px; height: 100%;
    background: linear-gradient(180deg, var(--peach-light) 0%, var(--peach) 100%);
    border-top: 3px solid #d8382f;
    overflow: hidden;
  }
  .ingredient-art {
    position: absolute; left: 10px; top: 20px; width: 480px; height: 300px;
    border-radius: 0 0 240px 240px / 0 0 160px 160px;
    background: linear-gradient(180deg, var(--art-top) 0%, var(--art-mid) 55%, var(--art-bottom) 100%);
  }
  .brand-mark-small {
    position: absolute; left: 0; right: 0; top: 24px; text-align: center;
    font-family: "Baloo 2", sans-serif; font-weight: 800; font-size: 24px; letter-spacing: 2px;
    color: var(--green-dark);
  }
  .brand-mark {
    position: absolute; left: 0; right: 0; top: 228px; text-align: center;
    font-family: "Baloo 2", sans-serif; font-weight: 800; font-size: 48px; letter-spacing: 2px;
    color: var(--green-dark);
  }
  .product-name {
    position: absolute; left: 0; right: 0; top: 318px; text-align: center;
    font-family: "Baloo 2", sans-serif; font-weight: 800; font-size: 62px; line-height: .92;
    color: var(--green-dark);
  }
  .tagline {
    position: absolute; left: 0; right: 0; top: 448px; text-align: center;
    font-family: "Caveat", cursive; font-weight: 700; font-size: 24px; color: var(--green-dark);
  }
  .veg-mark {
    position: absolute; right: 30px; top: 430px; width: 16px; height: 16px;
    border: 1.5px solid #2e8b3a; background: #fff; display: flex; align-items: center; justify-content: center;
  }
  .veg-mark span { width: 8px; height: 8px; border-radius: 50%; background: #2e8b3a; }
  .divider { position: absolute; left: 20px; right: 20px; top: 486px; height: 1px; background: var(--rule); }
  .contains {
    position: absolute; left: 22px; top: 500px; width: 260px;
    font-style: italic; font-size: 11px; line-height: 1.6; color: var(--ink);
  }
  .contains strong { font-weight: 600; }
  .gluten-free { position: absolute; left: 22px; top: 550px; font-style: italic; font-weight: 600; font-size: 10.5px; }
  .pack-count {
    position: absolute; right: 22px; top: 494px; width: 90px; height: 66px;
    background: var(--yellow); color: #fff; padding: 6px 0 0 7px;
    font-size: 9px; line-height: 1.1;
  }
  .pack-count b { display: block; font-size: 18px; font-weight: 600; }
  .pyramid-art {
    position: absolute; right: 0; top: 8px; width: 44px; height: 52px;
    background: linear-gradient(160deg, #f6f2ea, #cfc6b8 60%, #5a4a3e);
  }
</style>
</head>
<body>
<main class="box-net">

  <section class="side-panel">
    <div class="info-column">
      <p class="category">Proprietary Food: 14.1.5 Herbal Infusion</p>
      <p class="variant-name">Chocolate Truffle</p>
      <p class="ingredients"><span class="label">Ingredients:</span><br>
        Apple Pieces (33.50%), Cocoa (14%), Hibiscus Flowers (23%), Rosehip (9.75%), Blackberry Leaves, Carob-Fruit Pods, White Chocolate Pieces, Dehydrated Yoghurt Granules, Strawberry Fruit Pieces, Natural Flavouring Substances- Chocolate</p>
      <table class="nutrition">
        <tr><th colspan="3" class="table-title">Nutritional Information</th></tr>
        <tr><td colspan="3">Serving size - 200 ml (2 g)</td></tr>
        <tr><td colspan="3">Number of serving per pack - 20</td></tr>
        <tr><td></td><td>Per 100 g*</td><td>% RDA^</td></tr>
        <tr><td>Energy (kcal)</td><td class="num">354</td><td class="num">1</td></tr>
        <tr><td>Protein (g)</td><td class="num">5.87</td><td></td></tr>
        <tr><td>Carbohydrate (g)</td><td class="num">76.65</td><td></td></tr>
        <tr><td class="indent">Total Sugars (g)</td><td class="num">24.29</td><td></td></tr>
        <tr><td class="indent">Added Sugars (g)</td><td class="num">8.48</td><td class="num">0</td></tr>
        <tr><td>Total Fat (g)</td><td class="num">2.63</td><td class="num">0</td></tr>
        <tr><td class="indent">Saturated Fat (g)</td><td class="num">1</td><td class="num">0</td></tr>
        <tr><td class="indent">Trans Fat (g)</td><td class="num">0</td><td class="num">0</td></tr>
        <tr><td>Cholesterol (mg)</td><td class="num">0</td><td></td></tr>
        <tr><td>Sodium (mg)</td><td class="num">230.2</td><td class="num">0</td></tr>
        <tr><td>Calcium (mg)</td><td class="num">279.1</td><td></td></tr>
        <tr><td>Iron (mg)</td><td class="num">0</td><td></td></tr>
        <tr><td>Vitamin C (mg)</td><td class="num">30.96</td><td></td></tr>
        <tr><td colspan="3" class="foot">* approximate values<br>^ percent recommended daily values calculated on the basis of 2000 kcal diet</td></tr>
      </table>
    </div>

    <div class="legal-column">
      <p class="legal-block"><span class="label">Marketed by:</span> MERIDIAN LEAF TRADERS PVT LTD. 12 RIVERSIDE LANE, 2ND FLOOR, UNIT-204, KOLKATA-700017, Kolkata, West Bengal-700017</p>
      <span class="cert-mark"></span>
      <p class="lic">Lic No. 10000000004821</p>
      <p class="legal-block"><span class="label">Manufactured by:</span> BRIGHTFIELD INFUSIONS LLP SF NO. 51/4A, 7C LAKE VIEW ROAD, KOVAIPUDUR, Coimbatore Ward-12, Coimbatore, Tamil Nadu-641042</p>
      <span class="cert-mark"></span>
      <p class="lic">Lic No. 12400000007315</p>
      <p class="legal-block"><span class="label">Net Quantity:</span> 20 tea bags (40 g)</p>
      <p class="legal-block"><span class="label">Storage Instruction:</span> Store in airtight container, away from direct sunlight. Keep under refrigerated conditions for prolonged freshness.</p>
      <div class="consumer-care">
        <h4>Consumer care:</h4>
        <p class="care-row">
          <svg viewBox="0 0 10 10"><path d="M5 1a3 3 0 0 1 3 3c0 2-3 5-3 5S2 6 2 4a3 3 0 0 1 3-3z" fill="none" stroke="#4b4036" stroke-width=".8"/></svg>
          Refer to Marketer Address above.</p>
        <p class="care-row">
          <svg viewBox="0 0 10 10"><rect x="1" y="2.5" width="8" height="5" fill="none" stroke="#4b4036" stroke-width=".8"/><path d="M1 2.5l4 3 4-3" fill="none" stroke="#4b4036" stroke-width=".8"/></svg>
          hello@tulvotea.com</p>
        <p class="care-row">
          <svg viewBox="0 0 10 10"><path d="M2.5 1.5l1.5 2-1 1c.6 1.2 1.4 2 2.5 2.5l1-1 2 1.5-1 1.5C5 9 1 5 1 2.5z" fill="none" stroke="#4b4036" stroke-width=".8"/></svg>
          +91-33-40001234</p>
        <p class="care-row">
          <svg viewBox="0 0 10 10"><circle cx="5" cy="5" r="4" fill="none" stroke="#4b4036" stroke-width=".8"/><path d="M1 5h8M5 1c-2 2.5-2 5.5 0 8M5 1c2 2.5 2 5.5 0 8" fill="none" stroke="#4b4036" stroke-width=".6"/></svg>
          www.tulvotea.com</p>
      </div>
    </div>
  </section>

  <section class="front-panel">
    <div class="ingredient-art" role="img" aria-label="Illustration of the blend's ingredients: hibiscus flower, apple slices, strawberries, blackberries, rosehips, cocoa pod and white chocolate over loose tea"></div>
    <p class="brand-mark-small">TULVO</p>
    <p class="brand-mark">TULVO</p>
    <h1 class="product-name">Chocolate<br>Truffle</h1>
    <p class="tagline">move on</p>
    <div class="veg-mark"><span></span></div>
    <div class="divider"></div>
    <p class="contains"><strong>Contains:</strong> Apple Pieces, Cocoa, Hibiscus Flowers, Rosehip.</p>
    <p class="gluten-free">GLUTEN FREE</p>
    <div class="pack-count">
      <b>20</b>Pyramid<br>Tea Bags
      <div class="pyramid-art" role="img" aria-label="Pyramid tea bag filled with loose tea"></div>
    </div>
  </section>

</main>
</body>
</html>
```